Larkfield Circuitry LLC is a Minneapolis / St Paul and surrounding communities computer repair and service company. It serves residential and small businesses. We work primarily with virus removal, data recovery, system baselines, networking, and new system installation. The site should look clean, professional, and easy to navigate.

This wordpress project must be coded and integrated into a wordpress theme for easy upload and maintenance.
Updates

Designers - Please make sure your design is in a wordpress theme so that It can be uploaded.  

Thank you,

Brin 

Target Market(s)

Residential and Small Business

Industry/Entity Type

Residential

Requirements
Must have
• Site Content
1. Main Page should have photos that scroll across, Business Description, Space to run
“Specials” Ads
a. Intuitive Navigation
2. Additional Pages
a. Blog for Computer Repair Articles
b. Testimonials Page
c. Contact Pages
d. Services Page with the ability to put in pricing
3. The site must be clean and professional.
4. Wordpress Theme

```html
<!DOCTYPE html>
<html lang="en">
<head>
<meta charset="utf-8">
<title>Larkfield Circuitry LLC</title>
<link href="https://fonts.googleapis.com/css2?family=Telex&family=Arimo:wght@400;700&family=Oswald:wght@500;700&display=swap" rel="stylesheet">
<style>
:root{
  --green:#4a9a1c;
  --green-dark:#2f7410;
  --green-light:#7cc93a;
  --ink:#2b2b2b;
  --text:#3c3c3c;
  --bar:#262626;
  --panel:#d3d3d3;
  --panel-alt:#c7c7c7;
  --bg:#ececec;
  --white:#ffffff;
}
*{box-sizing:border-box;margin:0;padding:0}
html,body{width:1027px;height:1200px;overflow:hidden}
body{position:relative;background:linear-gradient(180deg,#f3f3f3 0%,var(--bg) 60%,#e6e6e6 100%);font-family:Arimo,Arial,sans-serif;color:var(--text);font-size:9.6px;line-height:1.45}
.abs,.ph{position:absolute}
.topline{left:0;top:0;width:1027px;height:3px;background:#3a3a3a}

.logo{left:152px;top:14px;display:flex;align-items:center;gap:8px}
.logo-mark{width:58px;height:58px;border-radius:50%;border:4px solid var(--green);background:var(--white)}
.logo-name{font-family:Telex,sans-serif;color:#4a4a4a;font-size:26px;line-height:1;letter-spacing:-.5px}
.logo-name small{display:block;font-size:12px;letter-spacing:.2px;margin-top:4px}

.phone{left:646px;top:30px;display:flex;align-items:center;gap:7px;font-size:18px;font-weight:700;color:var(--ink);letter-spacing:.5px}

.nav{left:151px;top:92px;width:726px;height:28px;background:var(--bar);border-radius:2px;display:flex;font-family:Telex,sans-serif;font-size:11.5px}
.nav a{color:#e8e8e8;text-decoration:none;padding:0 16px;line-height:28px;border-right:1px solid #3b3b3b}
.nav a.active{background:var(--green);color:var(--white);width:56px;text-align:center}
.nav a:last-child{border-right:none}

.social{left:991px;top:76px;width:36px;height:118px;background:var(--green);border-radius:3px 0 0 3px;padding:8px 7px;display:flex;flex-direction:column;gap:6px}
.social span{display:block;width:22px;height:20px;border-radius:3px;background:#f4f4f4}

.slider{left:151px;top:135px;width:726px;height:252px;background:radial-gradient(ellipse at 40% 45%,#3b3b3b 0%,#262626 70%);border-radius:3px;overflow:hidden}
.slide-title{left:27px;top:32px;font-size:43px;color:var(--white);letter-spacing:-.5px;line-height:1}
.slide-title em{font-style:normal;color:var(--green-light)}
.slide-tag{left:313px;top:78px;font-size:11px;color:#f0f0f0}
.slide-copy{left:28px;top:103px;width:460px;font-family:Telex,sans-serif;font-size:9px;letter-spacing:-.2px;line-height:16.5px;color:var(--green-light)}
.btn-grey{left:28px;top:165px;width:74px;height:23px;background:linear-gradient(#fafafa,#d8d8d8);border-radius:2px;font-size:11px;color:#333;text-align:center;line-height:23px}
.slide-offer{left:111px;top:169px;font-size:12.5px;font-weight:700;color:var(--white)}
.dots{left:27px;top:237px;display:flex;gap:4px}
.dots i{width:7px;height:7px;border-radius:50%;background:#eee;display:block}
.dots i.on{background:var(--green-light)}

.services{left:151px;top:430px;width:726px;height:178px;background:var(--panel);border-radius:3px;overflow:hidden;display:grid;grid-template-columns:repeat(5,1fr)}
.svc{border-right:1px solid #e2e2e2}
.svc:last-child{border-right:none}
.svc h3{height:39px;background:var(--bar);color:var(--white);font-size:10.6px;font-weight:700;display:flex;align-items:center;gap:6px;padding-left:9px;white-space:nowrap}
.svc h3 i,.svc li i{display:block;border-radius:50%;background:var(--green);flex:none}
.svc h3 i{width:11px;height:11px;box-shadow:inset 0 0 0 2px #7fce4a}
.svc ul{list-style:none}
.svc li{height:26px;display:flex;align-items:center;gap:7px;padding-left:8px;font-size:9.6px;color:#333;border-bottom:1px solid #e6e6e6}
.svc li:nth-child(even){background:var(--panel-alt)}
.svc li i{width:9px;height:9px;background:#86b86a}
.btn-green{display:inline-block;background:var(--green);color:var(--white);font-size:9px;padding:0 8px;height:18px;line-height:18px;border-radius:2px;border:1px solid var(--green-dark)}
.svc .btn-green{margin:6px 0 0 8px}

h2.section{position:absolute;font-family:Telex,sans-serif;font-weight:400;font-size:20px;color:var(--green);letter-spacing:-.2px}
.frame{position:absolute;border:3px solid #d6d6d6;outline:1px solid #bdbdbd}
.about-text{left:300px;top:652px;width:380px;line-height:14.6px}
.about-text p{margin-bottom:6px}

.article{position:absolute;left:151px;width:527px;height:143px;background:var(--white);padding:7px 8px}
.article h4{font-family:Telex,sans-serif;font-weight:400;font-size:15px;color:var(--ink)}
.article .meta{font-family:Telex,sans-serif;font-size:9.5px;color:var(--green);margin-top:1px}
.article .thumb{left:10px;top:49px;width:127px;height:77px}
.article .body{position:absolute;left:149px;top:47px;width:370px;line-height:14.6px}
.article .btn-green{margin-top:6px}

.ad1{left:695px;top:627px;width:182px;height:102px;background:linear-gradient(135deg,#f6f6f6,#d9d9d9);border-radius:3px;overflow:hidden}
.ad1 .copy{left:10px;top:6px;font-family:Oswald,sans-serif;color:#2d2d2d;line-height:1.05}
.ad1 .big{font-size:18px;font-weight:700}
.ad1 .small{font-size:10px;font-family:Arimo,sans-serif;font-weight:400}
.ad1 .mid{font-size:13px;font-weight:700}
.ad1 .view{left:10px;top:75px;background:#2c2c2c;color:#fff;font-size:8px;padding:1px 5px;border-radius:2px}
.ad2{left:695px;top:741px;width:182px;height:88px;background:linear-gradient(90deg,#1f1307,#6a3e0f 60%,#3a2207);border-radius:3px;overflow:hidden}
.ad2 .t{left:79px;top:10px;font-family:Oswald,sans-serif;font-weight:700;font-size:15px;color:#fff}
.ad2 .d{left:79px;top:34px;width:100px;font-size:9px;line-height:14px;color:#e8dccb}
.ad2 .c{left:80px;top:65px;font-size:9.5px;font-weight:700;color:#fff}

.testi{left:695px;top:873px;width:182px;height:170px;background:var(--white);border:1px solid #cdcdcd;border-radius:3px;padding:10px 10px}
.testi h5{font-size:9.3px;font-weight:700;color:#333;line-height:14.5px}
.testi blockquote{margin:14px 0 0 10px;font-size:9.5px;line-height:14.5px;color:#444;position:relative}
.quote{font-family:Georgia,serif;font-size:32px;color:#c9c9c9;position:absolute;line-height:1}
.who{left:22px;top:123px;display:flex;gap:8px;align-items:flex-start}
.who .av{width:36px;height:27px;background:linear-gradient(#e9d0a0,#b48a55);border:1px solid #bbb}
.who b{display:block;font-size:9.6px;font-weight:400;color:#222}
.who span{font-size:8.5px;font-style:italic;font-weight:700;color:var(--green)}

.footer{left:0;top:1147px;width:1027px;height:53px;background:var(--bar);color:#e4e4e4;font-size:8.6px;line-height:13.5px}
.footer .legal{left:151px;top:15px}
.footer .mark{left:826px;top:12px;display:flex;align-items:center;gap:5px;font-family:Telex,sans-serif;font-size:10px;color:#cfcfcf}
.footer .mark i{width:22px;height:22px;border-radius:50%;border:2px solid #9a9a9a;display:block}
</style>
</head>
<body>
<div class="abs topline"></div>

<div class="ph" role="img" aria-label="Illustration of a desktop tower, laptop and flying paper sheets" style="left:0;top:68px;width:148px;height:214px;background:linear-gradient(180deg,#e4e4e4,#d8d8d8)"></div>
<div class="ph" role="img" aria-label="Silhouette of a person seated at a computer desk" style="left:0;top:882px;width:141px;height:265px;background:linear-gradient(180deg,#5a5a5a,#2e2e2e)"></div>

<header>
  <div class="abs logo">
    <span class="logo-mark"></span>
    <div class="logo-name">Larkfield<small>Circuitry, LLC</small></div>
  </div>
  <div class="abs phone">
    <svg width="20" height="20" viewBox="0 0 20 20" aria-hidden="true"><circle cx="10" cy="10" r="9.5" fill="#5aa82a"/><path d="M6 7.5c0-1 .8-1.5 4-1.5s4 .5 4 1.5v1h-2.2v-1H8.2v1H6z M7 10h6l1 4H6z" fill="#fff"/></svg>
    +01 4407 2291
  </div>
  <div class="ph" role="img" aria-label="Cartoon support agent at a laptop" style="left:818px;top:0;width:60px;height:90px;background:linear-gradient(#d9c3a8,#9db3d4);border-radius:4px"></div>
  <nav class="abs nav">
    <a class="active" href="#">Home</a><a href="#">About Us</a><a href="#">Blog</a><a href="#">Services</a><a href="#">Testimonials</a><a href="#">Contact</a>
  </nav>
</header>

<div class="abs social" aria-label="Social links"><span></span><span></span><span></span><span></span></div>

<section class="abs slider">
  <div class="abs slide-title">Technical <em>SUPPORT</em></div>
  <div class="abs slide-tag">ANY TIME, ANY WHERE</div>
  <p class="abs slide-copy">Lorem Ipsum is simply dummy text of the printing and typesetting industry. Lorem Ipsum is simply Lorem Ipsum is simply dummy text of the printing and typesetting industry. Lorem Ipsum is simply dummy text of the printing and typesetting industry.</p>
  <div class="abs btn-grey">Learn More</div>
  <div class="abs slide-offer">Offering Execellent</div>
  <div class="abs dots"><i></i><i class="on"></i><i></i><i></i><i></i></div>
</section>
<div class="ph" role="img" aria-label="Photo of a black flat-screen monitor with keyboard" style="left:702px;top:103px;width:112px;height:316px;background:linear-gradient(180deg,#1c1c1c,#111);border-radius:2px"></div>

<section class="abs services">
  <div class="svc"><h3><i></i>VIRUS REMOVAL</h3><ul><li><i></i>Lorem Ipsum new data</li><li><i></i>$50 Ipsum new data</li><li><i></i>Lorem Ipsum new data</li><li><i></i>Lorem Ipsum new data</li></ul><span class="btn-green">Learn More</span></div>
  <div class="svc"><h3><i></i>DATA RECOVERY</h3><ul><li><i></i>Lorem Ipsum new data</li><li><i></i>$100 Ipsum new data</li><li><i></i>Lorem Ipsum new data</li><li><i></i>Lorem Ipsum new data</li></ul><span class="btn-green">Learn More</span></div>
  <div class="svc"><h3><i></i>SYSTEM BASELINES</h3><ul><li><i></i>Lorem Ipsum new data</li><li><i></i>$250 Ipsum new data</li><li><i></i>Lorem Ipsum new data</li><li><i></i>Lorem Ipsum new data</li></ul><span class="btn-green">Learn More</span></div>
  <div class="svc"><h3><i></i>NETWORKING</h3><ul><li><i></i>Lorem Ipsum new data</li><li><i></i>$85 sum new data</li><li><i></i>Lorem Ipsum new data</li><li><i></i>Lorem Ipsum new data</li></ul><span class="btn-green">Learn More</span></div>
  <div class="svc"><h3><i></i>INSTALLATION</h3><ul><li><i></i>Lorem Ipsum new data</li><li><i></i>$110 Ipsum new data</li><li><i></i>Lorem Ipsum new data</li><li><i></i>Lorem Ipsum new data</li></ul><span class="btn-green">Learn More</span></div>
</section>

<h2 class="section" style="left:151px;top:620px">About Larkfield Circuitry, LLC</h2>
<div class="frame" role="img" aria-label="Photo of a smiling man holding a laptop" style="left:151px;top:656px;width:137px;height:119px;background:linear-gradient(#f2f2f2,#c9ced6)"></div>
<div class="abs about-text">
  <p>There are many variations of passages of Lorem Ipsum available, but the majority fdgvfv suffered alteration in some form, by injected humour, or randomised words which don't look even slightly believable. If you are going to use a passage.</p>
  <p>Lorem Ipsum, you need to be sure there isn't anything embarrassing hidden in the middle of text. All the Lorem Ipsum generators on the Internet tend to repeat predefined chunks as necessary, making this the first true generator on the Internet.</p>
  <span class="btn-green">Learn More</span>
</div>

<h2 class="section" style="left:151px;top:797px">Computer Repair Articles</h2>
<article class="article" style="top:833px">
  <h4>Purchase as many Pay-as-you-go Credits</h4>
  <div class="meta">Date: 28.08.12 Tags: Computer, repaor, Virus Removal</div>
  <div class="frame thumb" role="img" aria-label="Photo of a smiling man with a laptop" style="background:linear-gradient(#f2f2f2,#c9ced6)"></div>
  <div class="body">There are many variations of passages of Lorem Ipsum available, but the majority have suffered alteration in some form, by injected humour, or randomised words which don't look even slightly believable. If you are going to use a passage. , or randomised words which don't look even slightly believable. If you are going to use a passage.<br><span class="btn-green">Learn More</span></div>
</article>
<article class="article" style="top:987px">
  <h4>Purchase as many Pay-as-you-go Credits</h4>
  <div class="meta">Date: 28.08.12 Tags: Computer, repaor, Virus Removal</div>
  <div class="frame thumb" role="img" aria-label="Photo of a smiling man with a laptop" style="background:linear-gradient(#f2f2f2,#c9ced6)"></div>
  <div class="body">There are many variations of passages of Lorem Ipsum available, but the majority have suffered alteration in some form, by injected humour, or randomised words which don't look even slightly believable. If you are going to use a passage. , or randomised words which don't look even slightly believable. If you are going to use a passage.<br><span class="btn-green">Learn More</span></div>
</article>

<aside>
  <div class="abs ad1">
    <div class="ph" role="img" aria-label="Photo of an open silver laptop" style="left:100px;top:14px;width:82px;height:88px;background:linear-gradient(180deg,#6a6a6a,#2a2a2a)"></div>
    <div class="abs copy"><div class="big">powerful</div><div class="small">performance</div><div class="mid"><span class="small">and </span>attractive</div><div class="mid">designs</div></div>
    <div class="abs view">View more</div>
  </div>
  <div class="abs ad2">
    <div class="ph" role="img" aria-label="Photo of a portable MP3 player" style="left:0;top:14px;width:72px;height:60px;background:linear-gradient(180deg,#3a3a3a,#151515)"></div>
    <div class="abs t">MP3/WMA/REC</div>
    <div class="abs d">Nulla facilisi. Vivamus ut justo nulla, sed lacinia</div>
    <div class="abs c">Click Here &nbsp;»</div>
  </div>
  <h2 class="section" style="left:695px;top:838px">Testimonials</h2>
  <div class="abs testi">
    <h5>LOREM IPSUM DOLOR CONSECTE TUR ADIPISCING</h5>
    <blockquote><span class="quote" style="left:-12px;top:-8px">“</span>Lorem ipsum dolor sit amet, ons ectetur adipiscing elit. Quisque quis tortor euismod ante ullam-corper consectetur id et est.<span class="quote" style="right:-4px;bottom:-20px">”</span></blockquote>
    <div class="abs who"><div class="av" role="img" aria-label="Customer portrait"></div><div><b>LOREM IPSUM</b><span>USA, WILLINTONG</span></div></div>
  </div>
  <svg class="abs" style="left:838px;top:1041px" width="20" height="14" viewBox="0 0 20 14" aria-hidden="true"><path d="M0 0h20L4 13z" fill="#fff" stroke="#cdcdcd"/><path d="M1 0h18" stroke="#fff" stroke-width="2"/></svg>
</aside>

<footer class="abs footer">
  <div class="abs legal">© 2012, All right reserved by Larkfield Circuitry, LLC<br>Terms &amp; Condition &nbsp; I &nbsp; Privacy Policy</div>
  <div class="abs mark"><i></i>Larkfield</div>
</footer>
</body>
</html>
```